This project is to address Personal Life issues/ Health & Wellness using a certified Professional Coaching Approach.

Major coaching areas include: Weight loss, Overwhelm/ Time Management, Increased Energy, Leadership, Improved Relationships, Finding Your Life Purpose & passion, Self Esteem & Confidence,

The combination of a board certified Internal Medicine physician and
professional coach is a powerful and unique approach to help people achieve
better health and well being.

Target Market(s)

Existing or potentially new patients/clients interested in any of the listed categories of coaching.

Industry/Entity Type

Life Coaching

Font styles to use
Sans Serif

Colors
00a990
0292cd
0255a3
33b8a4
a64599
6b449b
876aae
3176b5
33a6d7

Requirements
Must have
• Design specifics: Use of deep blues/greens using nature imagery is
• preferred- see our website for at Brightvalecare.com
• Each category of coaching must be listed out with a paragraph of description below each- I will provide the description in an attachment that is pending.
• Title of Brochure: "Clearbrook Health Personal Life & Wellness Coaching."
• "Coaching That Works!"
Nice to have
• A definition of coaching on the front of brochure:
• " A compassionate catalyzing relationship - The art of facilitating the performance, learning and development of another so they may achieve what the want faster.”
• Also on the front please place: "Stuck? Ask about a free coaching consult with Dr. Tavren to learn more!"
Should not have
• Should not have anything in the brochure that mentions medical services from the website outside of weight loss. The purpose of the brochure is to promote the coaching services.

```html
<!DOCTYPE html>
<html lang="en">
<head>
<meta charset="utf-8">
<title>Clearbrook Health Personal Life &amp; Wellness Coaching – Brochure Spread</title>
<link href="https://fonts.googleapis.com/css2?family=Arimo:wght@400;700&family=Oswald:wght@200;300&display=swap" rel="stylesheet">
<style>
  :root {
    --backdrop: #e4e4e4;
    --paper: #ffffff;
    --ink: #2a2a2a;
    --violet: #6b449b;
    --lavender: #876aae;
    --forest-dark: #1b2414;
    --forest-mid: #3f5a22;
    --bluebell: #4b3f9c;
    --sand: #ece9e4;
    --sand-light: #f6f5f2;
    --dusk-top: #b9a3b8;
    --dusk-mid: #7a5a86;
    --dusk-low: #4a3560;
  }
  * { box-sizing: border-box; margin: 0; padding: 0; }
  html, body { width: 1200px; height: 800px; overflow: hidden; }
  body {
    background: var(--backdrop);
    font-family: "Arimo", Arial, sans-serif;
    color: var(--ink);
  }
  .spread {
    position: absolute;
    left: 200px; top: 30px;
    width: 800px; height: 740px;
    display: flex;
    box-shadow: 0 8px 28px rgba(0,0,0,.18);
  }
  .panel { position: relative; width: 400px; height: 740px; overflow: hidden; }

  /* Cover panel */
  .cover-photo {
    position: absolute; inset: 0;
    background:
      radial-gradient(ellipse at 65% 70%, rgba(92,78,190,.85) 0%, rgba(75,63,156,.6) 35%, transparent 65%),
      radial-gradient(ellipse at 40% 25%, rgba(120,150,50,.55) 0%, transparent 55%),
      linear-gradient(180deg, var(--forest-dark) 0%, var(--forest-mid) 45%, var(--bluebell) 80%, #2f4a1e 100%);
  }
  .tagline {
    position: absolute; left: 44px; top: 58px;
    color: #fff;
    font-family: "Arimo", Arial, sans-serif;
    font-weight: 700;
    font-size: 15px;
    letter-spacing: 4px;
    line-height: 1.25;
    text-transform: uppercase;
  }
  .cover-title {
    position: absolute;
    right: 26px; top: 40px;
    writing-mode: vertical-rl;
    color: #fff;
    font-family: "Oswald", sans-serif;
    font-weight: 200;
    font-size: 27px;
    letter-spacing: 1.5px;
    text-transform: uppercase;
    white-space: nowrap;
  }

  /* Inside panel */
  .inside { background: var(--paper); }
  .beach-photo {
    position: absolute; left: 0; top: 0; width: 400px; height: 250px;
    background: linear-gradient(160deg, var(--sand-light) 0%, var(--sand) 60%, #ddd8d0 100%);
    clip-path: polygon(0 0, 100% 0, 100% 40%, 0 100%);
  }
  .section-label {
    position: absolute; left: 14px; top: 470px;
    writing-mode: vertical-rl;
    transform: rotate(180deg);
    font-family: "Oswald", sans-serif;
    font-weight: 200;
    font-size: 44px;
    letter-spacing: 3px;
    color: var(--violet);
  }
  .copy {
    position: absolute; left: 84px; top: 230px; width: 280px;
    font-size: 13px; line-height: 1.45;
  }
  .topic { margin-bottom: 22px; }
  .topic h2 { font-size: 13px; font-weight: 700; margin-bottom: 2px; }
  .mountain-photo {
    position: absolute; left: 0; bottom: 0; width: 400px; height: 220px;
    background: linear-gradient(180deg, var(--dusk-top) 0%, var(--dusk-mid) 55%, var(--dusk-low) 100%);
    clip-path: polygon(0 45%, 52% 100%, 0 100%);
  }
</style>
</head>
<body>
  <main class="spread">
    <section class="panel cover">
      <div class="cover-photo" role="img" aria-label="Photo of bluebells growing at the foot of woodland trees"></div>
      <p class="tagline">Coaching<br>That Works!</p>
      <h1 class="cover-title">Clearbrook Health Personal Life &amp; Wellness Coaching</h1>
    </section>

    <section class="panel inside">
      <div class="beach-photo" role="img" aria-label="Photo of people walking on a pale sandy beach"></div>
      <div class="section-label">LIFE</div>
      <div class="copy">
        <article class="topic">
          <h2>Finding Your Life Purpose</h2>
          <p>As a physician I have seen the direct link between life purpose and health. This is a major problem that is not addressed openly in our society, yet I see it on a daily basis. The consequences of lack of fulfillment have a profoundly negative effect. Fortunately, there is a method to exploring and discovering one's life purpose. It's part of my life's purpose to help you discover why you are here!</p>
        </article>
        <article class="topic">
          <h2>Confidence/Self Esteem</h2>
          <p>When we suffer from this condition we can never reach our potential. We are the story that we tell ourselves. Tell a different story and life becomes an unlimited adventure. Building confidence is a process.</p>
        </article>
      </div>
      <div class="mountain-photo" role="img" aria-label="Photo of misty purple mountain ridges at dusk"></div>
    </section>
  </main>
</body>
</html>
```